Marta Business Card

My wife is going to start her own business with renting holiday appartments to tourists. She needs a design for a new business card... and a new web site.
Look at Stayvolt "Erholung auf dem Lindenwäldchen"

Target Market(s)

Give business card to prospects at any situation

Contact Information for Business Card

not sure what this means

Font styles to use
Script

Colors
fec41a
fee18a

Requirements
Must have
• My wife's handwriting is difficult to read:
Entspannen - Loslassen - Auftanken
Marta & das Lindenwäldchen
Urlaub an einem besonderen Ort
Marta Brecke
Grauer Pfad 7
18471 Alt Feldow
post@marta-brecke.de
www.lindenwaeldchen.net
Nice to have
• Beige background
Font like handwriting

```html
<!DOCTYPE html>
<html lang="de">
<head>
<meta charset="utf-8">
<title>Marta &amp; das Lindenwäldchen – Visitenkarte</title>
<link rel="stylesheet" href="https://fonts.googleapis.com/css2?family=Mrs+Saint+Delafield&display=swap">
<style>
  :root {
    --page-bg: #e9e9e9;
    --card-beige: #fbeee0;
    --card-beige-deep: #f9e8d4;
    --card-white: #ffffff;
    --sun-yellow: #fec41a;
    --soft-yellow: #fee18a;
    --ink-grey: #8b8b8b;
    --shadow: 0 6px 14px rgba(0, 0, 0, 0.12);
  }
  * { box-sizing: border-box; margin: 0; padding: 0; }
  html, body {
    width: 1200px;
    height: 800px;
    overflow: hidden;
    background: var(--page-bg);
  }
  .sheet {
    width: 1200px;
    height: 800px;
    display: flex;
    align-items: center;
    justify-content: center;
    gap: 60px;
  }
  .card {
    position: relative;
    width: 500px;
    height: 310px;
    box-shadow: var(--shadow);
    overflow: hidden;
  }
  .beige-fill {
    background: linear-gradient(135deg, var(--card-beige) 0%, var(--card-beige-deep) 50%, var(--card-beige) 100%);
  }

  /* Back side */
  .card-back { background: var(--card-white); }
  .card-back .slogan-band {
    position: absolute;
    left: 0; top: 0;
    width: 100%;
    height: 168px;
    display: flex;
    align-items: center;
    justify-content: center;
    padding: 0 30px;
  }
  .slogan {
    font-family: "Mrs Saint Delafield", cursive;
    font-size: 42px;
    color: var(--ink-grey);
    font-weight: 400;
    white-space: nowrap;
  }
  .contact-area {
    position: absolute;
    left: 0; top: 168px;
    width: 100%;
    height: 142px;
    display: flex;
    justify-content: space-between;
    align-items: flex-start;
    padding: 30px 40px 0 56px;
  }
  .contact-block {
    font-family: "Mrs Saint Delafield", cursive;
    font-size: 24px;
    line-height: 1.35;
    color: var(--sun-yellow);
    font-style: normal;
    white-space: nowrap;
  }
  .contact-block.right { padding-top: 2px; }

  /* Front side */
  .card-front {
    display: flex;
    align-items: center;
    justify-content: center;
    padding: 0 36px;
  }
  .front-lockup {
    display: flex;
    flex-direction: column;
    align-items: flex-start;
  }
  .brand-name {
    font-family: "Mrs Saint Delafield", cursive;
    font-size: 46px;
    font-weight: 400;
    color: var(--sun-yellow);
    line-height: 1.1;
    white-space: nowrap;
  }
  .tagline {
    margin-top: 4px;
    margin-left: 56px;
    font-family: "Mrs Saint Delafield", cursive;
    font-size: 26px;
    color: var(--ink-grey);
    white-space: nowrap;
  }
</style>
</head>
<body>
  <main class="sheet">
    <section class="card card-back" aria-label="Visitenkarte Rückseite">
      <div class="slogan-band beige-fill">
        <p class="slogan">Urlaub an einem besonderen Ort</p>
      </div>
      <div class="contact-area">
        <address class="contact-block left">
          Marta Brecke<br>
          Grauer Pfad 7<br>
          18471 Alt Feldow
        </address>
        <address class="contact-block right">
          post@marta-brecke.de<br>
          www.lindenwaeldchen.net
        </address>
      </div>
    </section>

    <section class="card card-front beige-fill" aria-label="Visitenkarte Vorderseite">
      <div class="front-lockup">
        <h1 class="brand-name">Marta &amp; das Lindenwäldchen</h1>
        <p class="tagline">Entspannen - Loslassen - Auftanken</p>
      </div>
    </section>
  </main>
</body>
</html>
```